Vellandor Insurance & Consulting

We need a new business card designed.
Front Side:
Photo on left
Logo on top right
Name, title, company, and contact info aligned on right
Clean spacing with professional hierarchy

Back Side:
Tagline centered near the top:
Real expertise. Practical guidance. Reliable protection.

Coverage types centered below in 2 lines:
General Liability | Workers Comp | Commercial Auto
Property | Inland Marine | Excess Liability | Pollution

```html
<!DOCTYPE html>
<html lang="en">
<head>
<meta charset="utf-8">
<title>Vellandor Insurance &amp; Consulting – Business Card</title>
<link rel="stylesheet" href="https://fonts.googleapis.com/css2?family=Arimo:ital,wght@0,400;0,700;1,700&family=Crimson+Text:ital@1&display=swap">
<style>
  :root {
    --backdrop: #5b5b5b;
    --card: #ffffff;
    --ink: #000000;
    --text-dark: #222222;
    --band-grey: #8a8a8a;
    --accent: #f2b318;
    --on-dark: #ffffff;
  }
  * { box-sizing: border-box; margin: 0; padding: 0; }
  html, body {
    width: 1200px; height: 1200px; overflow: hidden;
    background: var(--backdrop);
    font-family: "Arimo", Arial, sans-serif;
  }
  .card {
    position: absolute;
    width: 690px; height: 394px;
    background: var(--card);
    overflow: hidden;
  }
  .card--front { left: 266px; top: 158px; }
  .card--back  { left: 262px; top: 651px; }

  /* Front */
  .wordmark {
    position: absolute; left: 0; right: 0; top: 92px;
    text-align: center; color: var(--ink);
    font-weight: 400;
  }
  .wordmark__mark {
    display: inline-block; width: 22px; height: 22px;
    border-radius: 50%; background: var(--ink);
    vertical-align: middle; margin-right: 14px;
  }
  .wordmark__name { font-size: 38px; letter-spacing: 4px; vertical-align: middle; }
  .wordmark__sub { display: block; font-size: 17px; letter-spacing: 1px; margin-top: 6px; padding-left: 36px; }

  .grey-band {
    position: absolute; left: 0; right: 0; top: 238px; height: 6px;
    background: var(--band-grey);
  }
  .info-panel {
    position: absolute; left: 0; right: 0; top: 246px; bottom: 0;
    background: var(--ink); color: var(--on-dark);
  }
  .identity {
    position: absolute; right: 362px; top: 40px; text-align: right;
  }
  .identity__name { font-size: 25px; font-weight: 700; letter-spacing: .3px; }
  .identity__title { font-family: "Crimson Text", Georgia, serif; font-style: italic; font-size: 17px; margin-top: 2px; }
  .identity__company { font-size: 16px; margin-top: 2px; }
  .divider {
    position: absolute; left: 344px; top: 36px; width: 1px; height: 82px;
    background: var(--on-dark);
  }
  .contact { position: absolute; left: 360px; top: 44px; list-style: none; }
  .contact li { display: flex; align-items: center; height: 20.5px; font-size: 16px; }
  .contact svg { width: 14px; height: 14px; margin-right: 12px; fill: var(--on-dark); flex: none; }

  /* Back */
  .back-wordmark {
    position: absolute; left: 0; right: 0; top: 118px;
    text-align: center; color: var(--ink); font-weight: 400;
  }
  .back-wordmark .wordmark__name { font-size: 44px; }
  .tagline {
    position: absolute; left: 0; right: 0; top: 281px;
    text-align: center; font-size: 17px; font-weight: 700; font-style: italic;
    color: var(--text-dark);
  }
  .rule {
    position: absolute; left: 50px; width: 590px; top: 307px; height: 1px;
    background: var(--accent);
  }
  .coverage {
    position: absolute; left: 0; right: 0; top: 314px;
    text-align: center; font-size: 17px; color: var(--text-dark); line-height: 22px;
  }
  .coverage .sep { color: var(--accent); margin: 0 5px; }
</style>
</head>
<body>
  <section class="card card--front">
    <div class="wordmark">
      <span class="wordmark__mark"></span><span class="wordmark__name">Vellandor</span>
      <span class="wordmark__sub">Insurance &amp; Consulting</span>
    </div>
    <div class="grey-band"></div>
    <div class="info-panel">
      <div class="identity">
        <p class="identity__name">Marisol Quintaro</p>
        <p class="identity__title">Agency Principal</p>
        <p class="identity__company">Brightpath Insurance</p>
      </div>
      <div class="divider"></div>
      <ul class="contact">
        <li><svg viewBox="0 0 24 24" aria-hidden="true"><path d="M6.6 10.8a15 15 0 0 0 6.6 6.6l2.2-2.2a1 1 0 0 1 1-.25 11.4 11.4 0 0 0 3.6.57 1 1 0 0 1 1 1V20a1 1 0 0 1-1 1A17 17 0 0 1 3 4a1 1 0 0 1 1-1h3.5a1 1 0 0 1 1 1c0 1.25.2 2.45.57 3.57a1 1 0 0 1-.25 1z"/></svg>(503) 555-0147</li>
        <li><svg viewBox="0 0 24 24" aria-hidden="true"><path d="M2 5h20v14H2z M4 7v.5l8 5.5 8-5.5V7z" fill-rule="evenodd"/></svg>Admin@Vellandorins.com</li>
        <li><svg viewBox="0 0 24 24" aria-hidden="true"><circle cx="12" cy="12" r="10"/></svg>www.VellandorInsurance.com</li>
      </ul>
    </div>
  </section>

  <section class="card card--back">
    <div class="back-wordmark">
      <span class="wordmark__mark"></span><span class="wordmark__name">Vellandor</span>
    </div>
    <p class="tagline">Real expertise. Practical guidance. Reliable protection.</p>
    <div class="rule"></div>
    <p class="coverage">
      General Liability<span class="sep">|</span>Workers Comp<span class="sep">|</span>Commercial Auto<span class="sep">|</span>Property<br>
      Inland Marine<span class="sep">|</span>Excess Liability<span class="sep">|</span>Pollution
    </p>
  </section>
</body>
</html>
```